International Biotech Startup needs a professionally looking web Design

We need a web design for a small biotech company based in Singapore which has global Pharma and Biotech Customers.

Our current website: www.zelvintralabs.com

However this was generated by few of us. We would require a professional design for biotech companies like us. The appearance of the website should be appealing to users and this is mainly a promotional website without any financial transactions.
Once the design is approved, we will provide the updated text.

Target Market(s)

Pharmaceutical, Biotech, healthcare

Industry/Entity Type

Biotechnology

Coding

Coded - Design and coding required

Number of Pages Required

5+ page

Requirements
Must have
• the website needs favicon.
Nice to have
• Please some of the companies websites that we like the most or they are in the similar domain. We would like to have something like that:
• http://www.pinecrestgenomics.com/
• http://www.marlowtherapeutics.com/
• http://www.tendrix.com/
• http://www.velunar.com/
• www.dornavil.com

```html
<!DOCTYPE html>
<html lang="en">
<head>
<meta charset="utf-8">
<title>Zelvintra Labs</title>
<link rel="stylesheet" href="https://fonts.googleapis.com/css2?family=Roboto:wght@300;400;500;700&display=swap">
<style>
:root{
  --yellow:#f7b30c;
  --orange:#f39b1e;
  --ink:#333;
  --muted:#666;
  --light:#efedeb;
  --grey:#ebebeb;
  --dark:#2a2727;
  --white:#fff;
}
*{box-sizing:border-box;margin:0;padding:0}
html,body{width:1200px;height:2917px;overflow:hidden}
body{position:relative;font-family:'Roboto',Arial,sans-serif;color:var(--ink);background:var(--white)}
.abs{position:absolute}
.hero{left:0;top:0;width:1200px;height:720px;background:linear-gradient(110deg,#3c4552 0%,#5a6270 30%,#8a8d96 55%,#6b4a4f 75%,#3a3438 100%)}
.hero-shade{left:0;top:0;width:1200px;height:720px;background:rgba(20,25,35,.35)}
.topbar{left:0;top:0;width:1200px;height:72px;font-size:13px;color:var(--white)}
.topbar .mail{position:absolute;left:100px;top:24px;display:flex;align-items:center;gap:8px}
.topbar .phone{position:absolute;left:947px;top:24px;display:flex;align-items:center;gap:8px}
.topbar .search{position:absolute;left:1088px;top:24px}
.navband{left:0;top:72px;width:1200px;height:93px;background:var(--yellow)}
.brand{position:absolute;left:104px;top:22px;display:flex;align-items:center;gap:10px;font-size:30px;font-weight:700;color:#2f4b8a;letter-spacing:.5px}
.brand .dot{width:22px;height:22px;border-radius:50%;background:#2f4b8a}
.nav{position:absolute;top:38px;left:0;font-size:15px;color:var(--white);text-transform:uppercase}
.nav a{position:absolute;white-space:nowrap;color:var(--white);text-decoration:none}
.nav a.on{color:#222}
.hero-title{left:0;top:415px;width:1200px;text-align:center;color:var(--white);font-weight:700;font-size:41px;line-height:57px;text-transform:uppercase}
.search-box{left:317px;top:568px;width:469px;height:72px;background:rgba(255,255,255,.82);font-size:16px;color:#666;padding:26px 36px}
.search-btn{left:786px;top:568px;width:93px;height:72px;background:#3a3330;display:flex;align-items:center;justify-content:center}
.rule{width:62px;height:5px;background:#333;left:569px}
.heading{left:0;width:1200px;text-align:center;color:var(--orange);font-size:40px;font-weight:300;text-transform:uppercase}
.para{font-size:12.5px;line-height:21px;color:var(--muted)}
.btn{background:var(--yellow);color:var(--white);font-size:12px;font-weight:700;text-transform:uppercase;display:flex;align-items:center;justify-content:center;border-radius:3px}
.divider{left:100px;top:985px;width:1000px;height:18px;background:radial-gradient(ellipse at top,rgba(0,0,0,.12),rgba(0,0,0,0) 70%)}
.building{left:101px;top:1048px;width:385px;height:317px;border:2px solid #ccc;background:linear-gradient(160deg,#9fc4ec 0%,#d7e6f5 35%,#8c97a4 60%,#4f5b68 100%)}
.acc{left:523px;width:578px;height:50px;background:#e4e4e4;display:flex;align-items:center}
.acc .ico{width:46px;height:50px;background:var(--yellow);display:flex;align-items:center;justify-content:center}
.acc .label{font-size:19px;color:#333;margin-left:16px;text-transform:uppercase}
.acc .hint{font-size:12px;color:#777;margin-left:36px}
.acc .toggle{position:absolute;right:12px;top:13px}
.about-band{left:0;top:1430px;width:1200px;height:509px;background:var(--light)}
.video{left:99px;top:1593px;width:475px;height:284px;background:radial-gradient(ellipse at 50% 55%,#2d5a5a 0%,#16213a 55%,#0e1426 100%)}
.press{top:1996px;width:190px;height:89px;background:#fff;border:1px solid #cfcfcf;border-radius:5px;display:flex;align-items:center;justify-content:center}
.press span{display:block;width:130px;height:34px;border-radius:3px;background:#d9dde3}
.testi-band{left:0;top:2136px;width:1200px;height:632px;background:var(--grey)}
.portrait{left:478px;top:2304px;width:246px;height:246px;border-radius:50%;border:4px solid #bbb;background:linear-gradient(180deg,#f2f2f2 0%,#d9d9d9 55%,#4a4d55 100%)}
.name{left:0;top:2584px;width:1200px;text-align:center;font-size:21px;color:#555}
.role{left:0;top:2612px;width:1200px;text-align:center;font-size:11px;font-weight:700;color:#333}
.quote{left:247px;top:2655px;width:706px;text-align:center;font-size:12px;line-height:21px;color:#444}
.qmark{font-size:48px;font-family:Georgia,serif;color:#333;line-height:1}
.footer{left:0;top:2768px;width:1200px;height:149px;background:var(--dark)}
.social{position:absolute;top:32px;width:36px;height:36px;border-radius:50%;background:var(--yellow)}
.foot-nav{position:absolute;top:86px;left:0;width:1200px;text-align:center;font-size:13px;color:#fff;text-transform:uppercase;letter-spacing:.3px}
.copy{position:absolute;top:111px;left:0;width:1200px;text-align:center;font-size:11px;color:#777}
</style>
</head>
<body>

<div class="abs hero" role="img" aria-label="Laboratory photograph with pipette and glassware"></div>
<div class="abs hero-shade"></div>

<header class="abs topbar">
  <div class="mail"><svg width="14" height="10" viewBox="0 0 14 10"><rect width="14" height="10" fill="#f7b30c"/><path d="M0 0 7 6 14 0" stroke="#333" fill="none"/></svg>hello@zelvintralabs.com</div>
  <div class="phone"><svg width="12" height="12" viewBox="0 0 12 12"><path d="M2 1l2 0 1 3-1.5 1a7 7 0 0 0 3.5 3.5L8 7l3 1 0 2c0 1-1 1.5-2 1.5A9 9 0 0 1 .5 3C.5 2 1 1 2 1z" fill="#f7b30c"/></svg>+44 (0) 200 481</div>
  <div class="search"><svg width="13" height="13" viewBox="0 0 13 13"><circle cx="5.5" cy="5.5" r="4" stroke="#f7b30c" stroke-width="2" fill="none"/><path d="M8.5 8.5 12 12" stroke="#f7b30c" stroke-width="2"/></svg></div>
</header>

<nav class="abs navband">
  <div class="brand"><span class="dot"></span>Zelvintra Labs</div>
  <div class="nav">
    <a class="on" style="left:471px">Home</a>
    <a style="left:564px">About</a>
    <a style="left:661px">Technology</a>
    <a style="left:809px">Products</a>
    <a style="left:935px">News</a>
    <a style="left:1031px">Contact</a>
  </div>
</nav>

<h1 class="abs hero-title">ZLV Technology and the<br>company has been featured in</h1>
<div class="abs search-box">Dummy text ever since the specimen book...</div>
<div class="abs search-btn"><svg width="34" height="34" viewBox="0 0 34 34"><circle cx="14" cy="14" r="10" stroke="#f7b30c" stroke-width="5" fill="none"/><path d="M21 21 31 31" stroke="#f7b30c" stroke-width="6" stroke-linecap="round"/></svg></div>

<section>
  <div class="abs rule" style="top:757px"></div>
  <h2 class="abs heading" style="top:770px">Welcome!</h2>
  <p class="abs para" style="left:175px;top:830px;width:850px;text-align:center">Zelvintra Labs is a Singapore-based synthetic biology company. We specialize in providing customized membrane protein products, services and expertise for drug discovery, diagnostics, and biomedical applications. Our company is backed by an international team of scientists, with diverse interdisciplinary backgrounds in synthetic chemistry, materials science, nanotechnology, cell signaling, and immunology. Our business team has extensive experience in biotechnology with a proven track record of working with small and big biotech and pharma companies all over the world.</p>
  <div class="abs btn" style="left:547px;top:930px;width:105px;height:43px">Read more</div>
</section>

<div class="abs divider"></div>

<section>
  <div class="abs building" role="img" aria-label="Glass office tower against blue sky"></div>
  <div class="abs acc" style="top:1046px">
    <div class="ico"><svg width="22" height="22" viewBox="0 0 22 22"><path d="M3 19l1-5L15 3l4 4L8 18z" fill="#fff"/></svg></div>
    <div class="label">Technology</div>
    <div class="hint">Nemo enim ipsam voluptatem quia voluptas sit aspernatur</div>
    <svg class="toggle" width="24" height="24" viewBox="0 0 24 24"><circle cx="12" cy="12" r="10" fill="none" stroke="#f7b30c" stroke-width="2"/><path d="M7 12h10M12 7v10" stroke="#f7b30c" stroke-width="2"/></svg>
  </div>
  <div class="abs acc" style="top:1111px">
    <div class="ico"><svg width="24" height="24" viewBox="0 0 24 24"><circle cx="10" cy="10" r="7" stroke="#fff" stroke-width="3" fill="none"/><path d="M15 15l7 7" stroke="#fff" stroke-width="3"/></svg></div>
    <div class="label">Products</div>
    <svg class="toggle" width="24" height="24" viewBox="0 0 24 24"><circle cx="12" cy="12" r="10" fill="none" stroke="#f7b30c" stroke-width="2"/><path d="M7 12h10" stroke="#f7b30c" stroke-width="2"/></svg>
  </div>
  <div class="abs para" style="left:583px;top:1176px;width:520px">
    <p>In addition to partnering with our clients in key areas of drug discovery, Zelvintra Labs also provides high-quality products per request for interested customers. Please let us know your needs via the Contact page, and our scientists will get back to you with more details.</p>
    <p style="color:#333;font-weight:500;margin-top:6px">Customized liposomes and polymersomes</p>
    <p>We provide liposomes using lipids, fluorophores and other reporter molecules or functional groups as required for specific projects. We also ship polymersomes that can be made with a wide.</p>
  </div>
  <div class="abs btn" style="left:583px;top:1323px;width:98px;height:39px;border-radius:8px">Read more</div>
</section>

<section>
  <div class="abs about-band"></div>
  <div class="abs rule" style="top:1490px"></div>
  <h2 class="abs heading" style="top:1502px">About us</h2>
  <div class="abs video" role="img" aria-label="Video preview about cells in drug screening">
    <svg class="abs" style="left:197px;top:102px" width="82" height="82" viewBox="0 0 82 82"><circle cx="41" cy="41" r="41" fill="rgba(255,255,255,.4)"/><path d="M32 24 58 41 32 58z" fill="#fff"/></svg>
    <div class="abs" style="left:16px;top:264px;width:443px;height:3px;background:rgba(255,255,255,.3)"></div>
  </div>
  <div class="abs para" style="left:609px;top:1582px;width:496px;text-align:justify">
    <p>Zelvintra Labs is a biotech startup, with its main office and R&amp;D lab in Singapore. Our company uses the artificial cell membrane (ZLV) platform to produce tailor-made products and programs centered around 'hard targets' in drug discovery. Typically, these are membrane protein targets that cannot be reliably produced using cell-lines.</p>
    <p style="margin-top:21px">The mission of Zelvintra Labs is to de-risk early stage drug discovery by significantly lowering the costs and time required for drug and antibody screening. Our area of expertise is focused on developing of new screening technologies using properties unique to the ZLV matrix. ZLV technology is also used in industry-standard assays and enables high-throughput screening at a scale not achievable by current platforms.</p>
  </div>
  <div class="abs btn" style="left:609px;top:1822px;width:116px;height:45px;border-radius:0">View more</div>
</section>

<section>
  <div class="abs press" style="left:99px"><span></span></div>
  <div class="abs press" style="left:301px"><span></span></div>
  <div class="abs press" style="left:506px"><span></span></div>
  <div class="abs press" style="left:708px"><span></span></div>
  <div class="abs press" style="left:912px"><span></span></div>
</section>

<section>
  <div class="abs testi-band"></div>
  <div class="abs rule" style="top:2209px"></div>
  <h2 class="abs heading" style="top:2221px">Testimonials</h2>
  <svg class="abs" style="left:126px;top:2414px" width="48" height="26" viewBox="0 0 48 26"><path d="M47 13H2M13 2 2 13l11 11" stroke="#333" stroke-width="2" fill="none"/></svg>
  <svg class="abs" style="left:1026px;top:2414px" width="48" height="26" viewBox="0 0 48 26"><path d="M1 13h45M35 2l11 11-11 11" stroke="#333" stroke-width="2" fill="none"/></svg>
  <div class="abs portrait" role="img" aria-label="Portrait of client in suit"></div>
  <div class="abs name">DAN.K</div>
  <div class="abs role">manager</div>
  <span class="abs qmark" style="left:220px;top:2640px">“</span>
  <p class="abs quote">Dignissimos ducimus qui blanditiis praesentium voluptatum deleniti atque corrupti quos dolores et quas molestias excepturi sint occaecati cupiditate non provident, similique sunt in culpa qui officia deserunt mollitia animi, id est laborum et dolorum fuga. Et harum quidem rerum facilis est et expedita distinctio. Nam libero tempore, cum soluta nobis est eligendi optio cumque</p>
  <span class="abs qmark" style="left:868px;top:2678px">”</span>
</section>

<footer class="abs footer">
  <span class="social" style="left:521px"></span>
  <span class="social" style="left:562px"></span>
  <span class="social" style="left:602px"></span>
  <span class="social" style="left:643px"></span>
  <div class="foot-nav">Home / &nbsp;About / &nbsp;Technology / &nbsp;Products / &nbsp;News / &nbsp;Contact</div>
  <div class="copy">Copyright © Zelvintra Labs 2014. All rights reserved.</div>
</footer>

</body>
</html>
```